Quorvane - New design for a couple of our pages

We need a total renovation of one of our webpages. First we would like the "insight and analysis" to be redesigned- for now we think the page is ok, but we want it to be great. We want this design to

We specialize in business intelligence and business management software. We are open for removal of some of the text on the site. Generally, we want the page to reflect that we are a modern technology company. See the frontpage of the website for common colors, however, we are open for better ones. We also need the design implemented on our site. If the page becomes a success, then there is a good chance that we would like a similar design for the other pages as well.Se link for the page that we need improved:https://www.quorvane.example/project/innsikt-og-analyse/?lang=en

Our main page also needs to be improved, here you will find our color palette, we would like more modern colors.

Sites we want to see with the new design suggestion:

Main page:
https://www.quorvane.example/

about us:
https://www.quorvane.example/aboutus/?lang=en

Finance and planning:
https://www.quorvane.example/project/finance-and-planning/?lang=en

Retail:
https://www.quorvane.example/project/retail/?lang=en

Target Market(s)

30 + / Business oriented / Desicion makers / financial officers / Educated

Industry/Entity Type

Information Technology

Number of Pages Required

5+ page

Font styles to use
Sans Serif

Requirements
Must have
• - Overall, we want the page to trigger the visitor to call us and schedule a meeting.
Nice to have
• Nice to have a sugguestion for a call to action - e.g. contact form. We are open to remove text and add another level of paiges under this one - again, open for suggestions for the content as well.
• We want similar colors to the already used greens and blue shades - but the designer may improble the color selection. Perhaps the designer can suggest a few options.

```html
<!DOCTYPE html>
<html lang="en">
<head>
<meta charset="utf-8">
<title>Quorvane – Intuitive Dashboards</title>
<link href="https://fonts.googleapis.com/css2?family=Roboto:wght@300;400;500;700&display=swap" rel="stylesheet">
<style>
:root{
  --teal:#2b7c96;
  --teal-dark:#1d6680;
  --green:#27a58c;
  --ink:#2f3437;
  --muted:#9aa1a6;
  --line:#e6e9eb;
  --soft:#f7f8f9;
  --canvas:#eef1f3;
  --violet:#5b4fe0;
  --amber:#f6b21b;
}
*{box-sizing:border-box;margin:0;padding:0}
html,body{width:1200px;height:1200px;overflow:hidden;background:var(--canvas);font-family:'Roboto',sans-serif;color:var(--ink)}
.stage{position:relative;width:1200px;height:1200px}
.page{position:absolute;left:370px;top:2px;width:940px;height:2440px;background:#fff;transform:scale(.49);transform-origin:0 0;overflow:hidden;box-shadow:0 6px 30px rgba(0,0,0,.12)}
.abs{position:absolute}
/* header */
.site-header{position:absolute;left:0;top:0;width:940px;height:60px}
.brand{position:absolute;left:130px;top:14px;display:flex;align-items:center;gap:8px;font-weight:700;font-size:22px;color:var(--ink)}
.brand i{width:10px;height:10px;background:var(--teal);display:block}
.nav{position:absolute;right:130px;top:22px;display:flex;gap:22px;font-size:10px;color:#555}
/* hero */
.hero{position:absolute;left:0;top:0;width:940px;height:527px}
.hero h1{position:absolute;left:130px;top:180px;font-weight:400;font-size:25px;line-height:27px;color:var(--teal);letter-spacing:.5px}
.hero h1 span{border-bottom:2px solid var(--teal)}
.hero .sub{position:absolute;left:130px;top:240px;font-size:10.5px;color:#555;letter-spacing:.3px}
.hero p{position:absolute;left:130px;top:264px;width:225px;font-size:8px;line-height:12px;color:var(--muted)}
.btn{display:inline-block;background:var(--teal);color:#fff;font-size:7px;text-transform:uppercase;letter-spacing:.3px;text-align:center;line-height:17px;height:17px}
.btn-outline{background:#fff;color:var(--teal);border:1px solid var(--teal);line-height:15px}
.hero .actions{position:absolute;left:130px;top:348px;display:flex;align-items:center;gap:10px;font-size:7px;color:var(--muted)}
.hero .actions .btn{width:95px}
.art{border-radius:10px}
/* services */
.services{position:absolute;left:0;top:527px;width:940px;height:181px;background:var(--soft)}
.service{position:absolute;width:200px;text-align:center;font-size:6.5px;color:#777;text-transform:uppercase;letter-spacing:.3px}
.service svg{display:block;margin:0 auto 6px;width:24px;height:24px;stroke:var(--green);fill:none;stroke-width:1.6}
/* features */
.feature h2{font-weight:400;font-size:16px;color:var(--ink)}
.feature p{font-size:7.5px;line-height:10px;color:#777;margin:6px 0 12px;width:260px}
.feature .btn{width:95px}
.dot{position:absolute;border:1.5px solid #6fb9ad;border-radius:50%}
.tri{position:absolute;width:0;height:0;border-left:4px solid transparent;border-right:4px solid transparent;border-top:7px solid #3aa692}
/* news */
.news{position:absolute;left:0;top:1505px;width:940px;height:388px;background:#fafafa}
.news h3{position:absolute;left:0;top:42px;width:940px;text-align:center;font-weight:400;font-size:15px}
.card{position:absolute;top:86px;width:164px;height:217px;background:#fff;text-align:center}
.card .photo{height:96px;background:linear-gradient(180deg,#8d9a92 0%,#5d6863 55%,#2f3532 100%)}
.card h4{font-size:7px;font-weight:500;margin:12px 0 8px}
.card p{font-size:6px;line-height:8.5px;color:#888;padding:0 10px}
.card .btn{width:94px;margin-top:18px;font-size:6px;line-height:15px;height:15px}
/* contact */
.contact{position:absolute;left:0;top:1893px;width:940px;height:389px;background:linear-gradient(180deg,#1f6d7d 0%,#237f83 45%,#2b8f86 100%)}
.contact h3{position:absolute;top:42px;width:940px;text-align:center;color:#fff;font-weight:400;font-size:16px}
.contact .lead{position:absolute;top:78px;width:940px;text-align:center;color:#dff2ef;font-size:6.5px}
.contact .talk{position:absolute;left:423px;top:94px;width:95px;background:#3aa1c0;font-size:6px;text-transform:none}
.field{position:absolute;left:306px;width:328px;color:#e6f4f2;font-size:6.5px;border-bottom:1px solid rgba(255,255,255,.35);padding-bottom:4px}
.contact .submit{position:absolute;left:423px;top:343px;width:95px;background:#3aa1c0;font-size:6px;text-transform:lowercase}
/* footer */
.site-footer{position:absolute;left:0;top:2282px;width:940px;height:158px;background:#fff}
.fcol{position:absolute;top:18px;font-size:6px;line-height:10px;color:#666}
.fcol b{display:block;font-weight:500;color:var(--ink);font-size:6.5px}
.social{position:absolute;left:648px;top:118px;display:flex;gap:14px}
.social span{width:10px;height:10px;border:1px solid #8a9ea5;border-radius:2px}
.copy{position:absolute;top:143px;width:940px;text-align:center;font-size:5.5px;color:#888}
</style>
</head>
<body>
<div class="stage">
<div class="page">

  <section class="hero">
    <svg class="abs" style="left:0;top:290px" width="320" height="237" viewBox="0 0 320 237">
      <defs><linearGradient id="heroBlob" x1="0" y1="0" x2="1" y2="1"><stop offset="0" stop-color="#22627f"/><stop offset="1" stop-color="#2c8e94"/></linearGradient></defs>
      <path d="M0 55 C40 40 80 70 95 125 C110 175 190 170 265 200 C295 212 310 225 320 237 L0 237 Z" fill="url(#heroBlob)"/>
    </svg>
    <header class="site-header">
      <div class="brand"><i></i>Quorvane</div>
      <nav class="nav"><span>Home</span><span>Industries</span><span>Solutions</span><span>Courses</span><span>Customers</span><span>About us</span></nav>
    </header>
    <h1><span>INTUITIVE</span><br><span>DASHBOARDS</span></h1>
    <div class="sub">FOR ENTERPRISE MANAGEMENT</div>
    <p>As end users and decision-makers you can access information from different sources in a clear and intuitive way. This enables you to make better and faster decisions on the basis of up-to-date and actual data. Reporting has never been easier – access it anytime, anywhere.</p>
    <div class="actions"><span class="btn">Join us now</span>or<span class="btn btn-outline">Read more</span></div>
    <div class="abs art" role="img" aria-label="Isometric illustration of a team around bar charts, a pie chart and a presentation board" style="left:440px;top:150px;width:430px;height:360px;background:radial-gradient(circle at 45% 60%,#f6b21b 0 18%,transparent 19%),linear-gradient(135deg,#6a5cf0 0%,#3b2fb8 55%,#eef0fb 56%,#f7f8fd 100%)"></div>
  </section>

  <section class="services">
    <div class="service" style="left:170px;top:20px"><svg viewBox="0 0 24 24"><path d="M9 18h6M10 21h4M12 3a6 6 0 0 0-4 10.5c1 1 1 2 1 3h6c0-1 0-2 1-3A6 6 0 0 0 12 3z"/></svg>Insight and analysis</div>
    <div class="service" style="left:370px;top:20px"><svg viewBox="0 0 24 24"><path d="M3 3v18h18M6 15l4-5 4 3 6-7"/></svg>Finance and planning</div>
    <div class="service" style="left:570px;top:20px"><svg viewBox="0 0 24 24"><rect x="4" y="3" width="16" height="5"/><rect x="4" y="10" width="16" height="5"/><rect x="4" y="17" width="16" height="4"/></svg>Network and system development</div>
    <div class="service" style="left:170px;top:95px"><svg viewBox="0 0 24 24"><path d="M12 3l8 4-8 4-8-4zM4 7v9l8 4 8-4V7M12 11v9"/></svg>Courses</div>
    <div class="service" style="left:370px;top:95px"><svg viewBox="0 0 24 24"><rect x="3" y="4" width="18" height="12"/><path d="M9 20h6M12 16v4"/></svg>Quorvane software</div>
    <div class="service" style="left:570px;top:95px"><svg viewBox="0 0 24 24"><circle cx="12" cy="12" r="9"/></svg>Advice and services</div>
  </section>

  <svg class="abs" style="left:760px;top:708px" width="180" height="230" viewBox="0 0 180 230">
    <circle cx="150" cy="75" r="90" fill="none" stroke="#bfe3dc" stroke-width="1.5"/>
    <circle cx="150" cy="75" r="105" fill="none" stroke="#d7eeea" stroke-width="1.2"/>
    <circle cx="150" cy="55" r="75" fill="#2ba58f"/>
  </svg>
  <span class="dot" style="left:75px;top:1057px;width:10px;height:10px"></span>
  <span class="dot" style="left:188px;top:1030px;width:8px;height:8px"></span>
  <span class="dot" style="left:900px;top:1253px;width:18px;height:18px"></span>
  <span class="dot" style="left:130px;top:1483px;width:8px;height:8px"></span>
  <span class="tri" style="left:18px;top:938px"></span>
  <span class="tri" style="left:880px;top:955px"></span>
  <span class="tri" style="left:5px;top:1410px"></span>
  <span class="tri" style="left:870px;top:1425px"></span>

  <div class="abs art" role="img" aria-label="Illustration of a monitor showing a data chart beside a standing person and plants" style="left:150px;top:778px;width:310px;height:190px;background:linear-gradient(180deg,#f3f4f5 0%,#e9ebee 100%)"></div>
  <div class="feature abs" style="left:474px;top:822px">
    <h2>Get the most out of your business data</h2>
    <p>Discover trends, make profitable decisions, get quick access to key figures all with Quorvane Business Intelligence.</p>
    <span class="btn">Join us now</span>
  </div>

  <div class="feature abs" style="left:130px;top:1077px">
    <h2>Become more competitive</h2>
    <p>Get the best budget, forecast, analysis, financial modeling, business intelligence and much more.</p>
    <span class="btn">Join us now</span>
  </div>
  <div class="abs art" role="img" aria-label="Illustration of a person presenting charts on a large browser window" style="left:486px;top:1020px;width:305px;height:225px;background:linear-gradient(135deg,#eef0fb 0%,#dfe3f7 60%,#c9cff2 100%)"></div>

  <div class="abs art" role="img" aria-label="Illustration of a laptop with bar and line charts beside a standing person" style="left:132px;top:1292px;width:330px;height:180px;background:linear-gradient(135deg,#eceefb 0%,#c7cdf6 55%,#8c93ee 100%)"></div>
  <div class="feature abs" style="left:474px;top:1342px">
    <h2>Quorvane Loan administration</h2>
    <p>Get full control of your loan portfolio with Quorvane Loan Administration.</p>
    <span class="btn">Join us now</span>
  </div>

  <section class="news">
    <svg class="abs" style="left:0;top:206px" width="200" height="182" viewBox="0 0 200 182">
      <defs><linearGradient id="newsBlob" x1="0" y1="0" x2="1" y2="1"><stop offset="0" stop-color="#22627f"/><stop offset="1" stop-color="#2c8e94"/></linearGradient></defs>
      <path d="M0 5 C40 -5 70 20 75 70 C80 120 140 130 190 182 L0 182 Z" fill="url(#newsBlob)"/>
    </svg>
    <h3>Latest News</h3>
    <article class="card" style="left:130px"><div class="photo" role="img" aria-label="Photo of a presenter in front of an audience"></div><h4>More value of your data</h4><p>Quorvane provides you with the insight you need to make the good decisions that give your business added value and growth.</p><span class="btn">Read More</span></article>
    <article class="card" style="left:304px"><div class="photo" role="img" aria-label="Photo of a presenter in front of an audience"></div><h4>More value of your data</h4><p>Quorvane provides you with the insight you need to make the good decisions that give your business added value and growth.</p><span class="btn">Read More</span></article>
    <article class="card" style="left:478px"><div class="photo" role="img" aria-label="Photo of a presenter in front of an audience"></div><h4>More value of your data</h4><p>Quorvane provides you with the insight you need to make the good decisions that give your business added value and growth.</p><span class="btn">Read More</span></article>
    <article class="card" style="left:652px"><div class="photo" role="img" aria-label="Photo of a presenter in front of an audience"></div><h4>More value of your data</h4><p>Quorvane provides you with the insight you need to make the good decisions that give your business added value and growth.</p><span class="btn">Read More</span></article>
  </section>

  <section class="contact" role="img" aria-label="Contact section over a tinted photo of an empty meeting room">
    <h3>Contact Us</h3>
    <div class="lead">Want to talk to someone now? Chat with a member of our team. Hours 8am–4pm (CET)</div>
    <span class="btn talk">Let's Talk</span>
    <div class="field" style="top:160px">Name</div>
    <div class="field" style="top:193px">Email</div>
    <div class="field" style="top:226px;height:90px">Message</div>
    <span class="btn submit">submit</span>
  </section>

  <footer class="site-footer">
    <div class="fcol" style="left:130px"><b>Industries</b>Banking, Finance &amp; Insurance<br>Retail<br>Property<br>Energy<br>Health<br>Oil &amp; Offshore<br>Production<br>Shipping</div>
    <div class="fcol" style="left:302px"><b>Solutions</b>Insight &amp; Analysis<br>Finance &amp; Planning<br>Cloud &amp; System Development<br>Quorvane Software<br>Advice</div>
    <div class="fcol" style="left:474px"><b>Courses</b>Course calendar<br>Internal Corporate Courses<br><br><b>Customers</b>All Customers<br>Customer stories</div>
    <div class="fcol" style="left:646px"><b>More Information</b>About us<br>Career<br>Contact us<br>Customer Support<br>News<br>Partners</div>
    <div class="social"><span></span><span></span><span></span></div>
    <div class="copy">Copyright 2019 Quorvane AS all rights reserved | T: +47 00 00 00 00 | E: post@quorvane.example</div>
  </footer>

</div>
</div>
</body>
</html>
```